Medical Prescription for Diagnostic Sleep Testing

Tamber Ridge Vital Labs main marketing tool is our Prescription that we leave with medical providers. Prescription is printed on 8.5 x 11 sheets of paper to create a prescription pad for our medical providers. Prescription should fit to one page. Tamber Ridge Vital Labs works with 250 different medical providers so it is important we are able to update and change the medical provider information at bottom. The medical provider would fill-out top with patient information, check-off center testing and patient co-morbidity and Fax to Tamber Ridge Vital Labs. Because it is Faxed to us it is important to have clear print and large font Attached or uploaded file is one example we currently use. Please review all 5 must haves.

Target Market(s)

Prescription for medical providers to fill-out and fax to Tamber Ridge Vital Labs to conduct the sleep study.

Industry/Entity Type

Medical

Colors

Designer to choose only greyscale colors for use in the design.

Requirements
Must have
• 1) Prescription Size: 8.5 x 11
• 2) Must fit to One page Only
• 3) Ability to change medical provider information at bottom of prescription. We work with 250 different medical providers
• 4) Ability to change or update any part of prescription
• 5) Document Must be created in Microsoft Word 2016. This is the program we use for our prescriptions.
Nice to have
• Can be done in Gray-Scale or Black and White since its being faxed from the medical provider to us.

```html
<!DOCTYPE html>
<html lang="en">
<head>
<meta charset="utf-8">
<title>Sleep Study Physician Order</title>
<link href="https://fonts.googleapis.com/css2?family=Carlito:ital,wght@0,400;0,700;1,400&family=Tinos:ital@0;1&family=Caladea:wght@400;700&family=Cinzel:wght@500&family=Arimo:wght@400;700&display=swap" rel="stylesheet">
<style>
:root{
  --backdrop:#b4b4b4;
  --paper:#ffffff;
  --ink:#111111;
  --muted:#555555;
  --brand:#333333;
  --band:#e4e4e4;
}
*{box-sizing:border-box;margin:0;padding:0}
html,body{width:1200px;height:1200px;overflow:hidden;background:var(--backdrop)}
.sheet{position:absolute;left:191px;top:70px;width:818px;height:1059px;background:var(--paper);color:var(--ink);font-family:'Carlito',sans-serif}
.abs{position:absolute;white-space:nowrap}
.brand-block{left:24px;top:22px;width:190px;height:118px;border:2px solid var(--brand);border-radius:6px;display:flex;flex-direction:column;align-items:center;justify-content:center;gap:8px}
.brand-name{font-family:'Carlito',sans-serif;font-weight:700;font-size:19px;line-height:1.15;color:var(--brand);text-align:center;white-space:normal}
.brand-badge{width:26px;height:20px;background:var(--brand)}
.title{left:303px;top:42px;font-family:'Cinzel',serif;font-weight:500;font-size:25px;color:var(--brand);letter-spacing:.2px}
.contact{left:233px;width:480px;text-align:center;font-weight:700;font-size:17px}
.field{font-family:'Tinos',serif;font-size:15px;display:flex;align-items:flex-end}
.field .line{display:inline-block;border-bottom:1px solid var(--ink);height:14px;margin-left:2px}
.rule{left:46px;width:738px;height:2px;background:var(--ink)}
.section-title{left:0;width:818px;text-align:center;font-weight:700;font-size:20px;padding-left:10px}
.box{display:inline-block;width:12px;height:12px;border:1.5px solid var(--ink);box-shadow:2px 2px 0 var(--ink);margin-right:8px;vertical-align:-1px}
.order{font-size:17.5px}
.note{font-family:'Arimo',sans-serif;font-size:11px;font-style:italic}
.sub{font-family:'Arimo',sans-serif;font-size:10.5px}
.necessity{left:48px;top:570px;width:751px;height:178px;border:1px solid var(--ink)}
.necessity-head{height:19px;background:var(--band);border-bottom:1px solid var(--ink);text-align:center;font-family:'Caladea',serif;font-weight:700;font-size:14.5px;line-height:19px;margin-right:-3px;border-right:1px solid var(--ink)}
.necessity-cols{display:flex;height:158px}
.necessity-col{list-style:none;font-family:'Caladea',serif;font-size:13px;line-height:17px;padding:2px 0 0 9px}
.necessity-col + .necessity-col{border-left:1px solid var(--ink)}
.necessity-col .box{width:9px;height:9px;border-width:1.2px;box-shadow:1.5px 1.5px 0 var(--ink);margin-right:5px;vertical-align:0}
.clinic{left:0;width:818px;text-align:center}
.provider{font-weight:700;font-size:15.5px}
.provider .box{width:13px;height:13px}
.npi{font-family:'Arimo',sans-serif;font-weight:700;font-size:11.5px;color:#333;transform:scaleX(.88);transform-origin:left}
.thanks{left:0;width:818px;text-align:center;font-family:'Tinos',serif;font-style:italic;font-size:17px}
</style>
</head>
<body>
<main class="sheet">
  <div class="abs brand-block">
    <div class="brand-name">Tamber Ridge<br>Vital Labs</div>
    <div class="brand-badge" role="img" aria-label="Accreditation badge"></div>
  </div>
  <h1 class="abs title">SLEEP STUDY PHYSICIAN ORDER</h1>
  <div class="abs contact" style="top:78px">Phone: (555) 214-3380 &nbsp;•&nbsp; Fax: (555) 214-3391</div>
  <div class="abs contact" style="top:101px">2480 W. Orchard Lane, Suite 7 - C; Fairhaven, NV 89002</div>

  <div class="abs field" style="left:48px;top:149px">Patient Name:<span class="line" style="width:370px"></span>DOB: <span class="line" style="width:78px;margin-left:4px"></span>/<span class="line" style="width:78px"></span>/<span class="line" style="width:68px"></span></div>
  <div class="abs field" style="left:48px;top:176px">Telephone: <span class="line" style="width:290px"></span>Alternate Telephone: <span class="line" style="width:230px;margin-left:4px"></span></div>
  <div class="abs field" style="left:48px;top:202px">Primary Insurance: <span class="line" style="width:238px"></span>Secondary Insurance: <span class="line" style="width:230px;margin-left:4px"></span></div>
  <div class="abs field" style="left:48px;top:229px">Height:<span class="line" style="width:176px"></span></div>
  <div class="abs field" style="left:302px;top:229px">Weight:<span class="line" style="width:146px"></span></div>
  <div class="abs field" style="left:559px;top:229px">Patient Gender&nbsp;<span style="font-size:9px">(circle one)</span>:&nbsp;&nbsp; M &nbsp; / &nbsp; F</div>
  <div class="abs rule" style="top:261px"></div>

  <h2 class="abs section-title" style="top:292px">Diagnostic Sleep Study Ordered</h2>
  <div class="abs order" style="left:76px;top:318px"><span class="box"></span><b style="text-decoration:underline;font-size:19px">COMPLETE <span style="font-size:16px">SLEEP STUDY</span></b><b>:</b> <i style="color:var(--muted);text-decoration:underline dotted">(Based on Insurance or Patient’s Choice)</i></div>
  <div class="abs" style="left:106px;top:348px;font-weight:700;font-size:15.5px">In-Lab Sleep Study (PSG) or Home Sleep Study <small style="font-weight:400;font-size:10.5px">(PSG 95810 / HST 95806)</small></div>
  <div class="abs" style="left:108px;top:372px;font-weight:700;font-size:15.5px">with follow-up PAP Titration Study <small style="font-weight:400;font-size:10.5px">(PAP 95811 if positive for sleep apnea)</small></div>
  <div class="abs order" style="left:83px;top:397px"><span class="box"></span>PEDIATRIC SLEEP STUDY: PSG w/End Tidal CO2 Monitoring</div>
  <div class="abs sub" style="left:107px;top:420px">(PSG 95782 under 6 years of age &amp; PSG 95810 older than 6 years of age)</div>
  <div class="abs order" style="left:83px;top:438px"><span class="box"></span>IN-LAB DIAGNOSTIC SLEEP STUDY/POLYSOMNOGRAM <span class="sub">(PSG 95810)</span></div>
  <div class="abs order" style="left:83px;top:464px"><span class="box"></span>SPLIT-NIGHT STUDY <span class="sub">(PSG with PAP 95810 &amp; 95811)</span> <span class="note" style="font-weight:700;text-decoration:underline;font-size:11.5px">To Comply With Accreditation &amp; Insurance Guidelines</span><span class="note">:</span></div>
  <div class="abs note" style="left:107px;top:487px">AHI must be 20 or greater with minimum 2 hour recorded sleep time and 3 hours minimum to complete PAP treatment.</div>
  <div class="abs order" style="left:83px;top:507px"><span class="box"></span>&nbsp;CPAP / BiPAP / BiPAP ST Titration Study <span class="sub">(Patients with documented sleep apnea 95811)</span></div>
  <div class="abs order" style="left:83px;top:534px"><span class="box"></span>&nbsp;Home Sleep Study <span class="sub">(HST 95806 Conducted in patient’s home &amp; unattended by technologist) (No insurance patient cost $250.00)</span></div>
  <div class="abs rule" style="top:564px"></div>

  <section class="abs necessity">
    <div class="necessity-head">Patient Medical Necessity – Please Check All Boxes That Apply</div>
    <div class="necessity-cols">
      <ul class="necessity-col" style="width:240px">
        <li><span class="box"></span>Atrial Fibrillation</li><li><span class="box"></span>Bipolar Disorder</li><li><span class="box"></span>Congestive Heart Failure</li><li><span class="box"></span>COPD</li><li><span class="box"></span>Depression</li><li><span class="box"></span>Excessive Daytime Sleepiness</li><li><span class="box"></span>Gasping Sensations with</li><li style="line-height:16px"><span class="box"></span>Frequent Awakenings</li><li><span class="box"></span>Frequent Urination</li>
      </ul>
      <ul class="necessity-col" style="width:232px">
        <li><span class="box"></span>Heart Disease</li><li><span class="box"></span>History Heart Attack</li><li><span class="box"></span>Hypertension</li><li><span class="box"></span>Insomnia</li><li><span class="box"></span>Mental or Mood Disorder</li><li><span class="box"></span>Loud Snoring</li><li><span class="box"></span>Morbid Obesity / Obesity</li><li><span class="box"></span>Morning Headaches</li><li><span class="box"></span>Narcolepsy</li>
      </ul>
      <ul class="necessity-col" style="flex:1">
        <li><span class="box"></span>Opioid Use</li><li><span class="box"></span>PTSD</li><li><span class="box"></span>Pulmonary Disease</li><li><span class="box"></span>Restless Leg Syndrome</li><li><span class="box"></span>Seizures</li><li><span class="box"></span>Shift Work Sleep disorder</li><li><span class="box"></span>Stroke / TIA</li><li><span class="box"></span>Witnessed Apnea</li><li><span class="box"></span>Other:<span style="display:inline-block;width:165px;border-bottom:1px solid var(--ink);height:11px"></span></li>
      </ul>
    </div>
  </section>
  <div class="abs rule" style="top:754px"></div>

  <h2 class="abs clinic" style="top:758px;font-size:22px;font-weight:700">Silverpine Ear + Sinus Clinic</h2>
  <div class="abs clinic" style="top:786px;font-size:13.5px">4175 N. Canyon Road; Fairhaven, NV 89004-2210 &nbsp;•&nbsp; Telephone: &nbsp;555-308-4420 &nbsp;&nbsp; Fax: &nbsp;555-308-4431</div>

  <div class="abs provider" style="left:50px;top:810px"><span class="box"></span>Dr. Marcus Ellery Thorne</div>
  <div class="abs npi" style="left:72px;top:830px">NPI: &nbsp;1000000117</div>
  <div class="abs provider" style="left:272px;top:810px"><span class="box"></span>Dr. Paul R. Westbrook</div>
  <div class="abs npi" style="left:294px;top:830px">NPI: 1000000224</div>
  <div class="abs provider" style="left:483px;top:810px"><span class="box"></span>Dr <i>Gordon L. Havelock</i></div>
  <div class="abs npi" style="left:505px;top:830px">NPI: 1000000331</div>
  <div class="abs provider" style="left:50px;top:849px"><span class="box"></span>Dr. Elena Marsh</div>
  <div class="abs npi" style="left:72px;top:869px">NPI: 1000000448</div>
  <div class="abs provider" style="left:272px;top:849px"><span class="box"></span>Rita Calloway, FNP-C</div>
  <div class="abs npi" style="left:294px;top:869px">NPI: 1000000555</div>
  <div class="abs provider" style="left:487px;top:849px"><span class="box" style="margin-right:2px"></span>Owen Pratt, PA-C</div>
  <div class="abs npi" style="left:508px;top:869px">NPI: 1000000662</div>

  <div class="abs field" style="left:45px;top:925px">Physician’s Signature:<span class="line" style="width:370px"></span>&nbsp;Date: <span class="line" style="width:56px;margin-left:4px"></span>/<span class="line" style="width:56px"></span>/<span class="line" style="width:56px"></span></div>
  <div class="abs clinic" style="top:946px;font-size:17.5px;font-weight:700">Please Fax: 555-214-3391 or Email: intake@tamberridgelabs.example</div>
  <div class="abs" style="left:45px;top:970px;font-size:14.5px">
    <svg width="13" height="13" viewBox="0 0 13 13" style="vertical-align:-1px;margin-right:4px"><rect x=".5" y=".5" width="12" height="12" fill="none" stroke="#111"/><path d="M3 6.5l2.5 2.5L10.5 2" fill="none" stroke="#111" stroke-width="1.2"/></svg>Fax Along With: Patient Demographic Information &nbsp;•&nbsp; Copy of Current Insurance Information &nbsp;•&nbsp; Clinical Notes</div>
  <div class="abs thanks" style="top:993px">Thank You For your support GLEN &amp; MARK</div>
</main>
</body>
</html>
```